Business card design needed

We design, manufacture and install kitchen robes vanity etc.
We have a current card that i want to upload that you can base the design around and make suggestions for other design but we need the logo to be unchanged that i will up load along with our current card.

Industry/Entity Type

Business

Contact Information for Business Card

Tallowind Joinery Works
Dorian Calvestri
47 Quarrington Avenue, Kestrelby S.A 5189
dorian@tallowindjoinery.com.au
Lic. No. Bld 582904 Bld 740251

```html
<!DOCTYPE html>
<html lang="en">
<head>
<meta charset="utf-8">
<title>Tallowind Joinery Works – Business Card</title>
<link rel="stylesheet" href="https://fonts.googleapis.com/css2?family=Old+Standard+TT:wght@700&family=Didact+Gothic&family=Arimo&display=swap">
<style>
  :root {
    --card-bg: #ffffff;
    --plum: #96005a;
    --sky: #53a9f0;
    --sun: #f7e21a;
    --leaf: #8cc63e;
    --ink: #111111;
  }
  * { margin: 0; padding: 0; box-sizing: border-box; }
  html, body { width: 1200px; height: 741px; overflow: hidden; background: var(--card-bg); }
  .card { position: relative; width: 1200px; height: 741px; background: var(--card-bg); overflow: hidden; }

  .card__side-art { position: absolute; left: 0; top: 0; width: 1200px; height: 741px; }
  .side-art__stop--plum { stop-color: var(--plum); }
  .side-art__stop--sky { stop-color: var(--sky); }
  .side-art__stop--sun { stop-color: var(--sun); }

  .brand-mark {
    position: absolute; left: 560px; top: 62px;
    display: flex; align-items: center; gap: 22px;
    font-family: "Old Standard TT", serif; font-weight: 700;
    font-size: 78px; line-height: 1; color: var(--leaf);
  }
  .brand-mark__dot { width: 26px; height: 26px; border-radius: 50%; background: var(--leaf); }

  .card__title { position: absolute; left: 0; top: 0; width: 1200px; height: 741px; pointer-events: none; }
  .card__title text {
    font-family: "Old Standard TT", serif; font-weight: 700;
    font-size: 84px; fill: var(--leaf);
  }

  .address {
    position: absolute; left: 566px; top: 428px;
    font-family: "Didact Gothic", sans-serif; font-size: 27px;
    line-height: 48px; color: var(--ink); font-style: normal;
  }
  .contact {
    position: absolute; left: 774px; top: 660px;
    font-family: "Arimo", sans-serif; font-size: 25px;
    line-height: 40px; color: var(--ink);
  }
</style>
</head>
<body>
<main class="card">
  <svg class="card__side-art" viewBox="0 0 1200 741" role="img" aria-label="Flowing plum, blue and yellow wave bands along the left edge">
    <defs>
      <linearGradient id="side-art-tones" x1="0" y1="0" x2="1" y2="0">
        <stop class="side-art__stop--plum" offset="0.45"/>
        <stop class="side-art__stop--sky" offset="0.72"/>
        <stop class="side-art__stop--sun" offset="1"/>
      </linearGradient>
    </defs>
    <path fill="url(#side-art-tones)" d="M0 0 H385 C370 140 300 240 240 340 C190 430 180 540 230 630 C260 690 320 725 380 741 H0 Z"/>
  </svg>

  <div class="brand-mark">
    <span class="brand-mark__dot"></span>
    <span class="brand-mark__name">Tallowind</span>
  </div>

  <svg class="card__title" viewBox="0 0 1200 741">
    <text x="338" y="330" textLength="836" lengthAdjust="spacingAndGlyphs">Tallowind Joinery Works Dorian Calvestri</text>
  </svg>

  <address class="address">
    47 Quarrington Avenue,<br>
    Kestrelby S.A 5189
  </address>

  <div class="contact">
    <div class="contact__email">dorian@tallowindjoinery.com.au</div>
    <div class="contact__licence">Lic. No. Bld 582904 Bld 740251</div>
  </div>
</main>
</body>
</html>
```